Dental Office Needs- Flyer Design for Same Day Crowns

We need a flyer that will explain the benefits of the same day crown from the patient prospective. Not show pictures of the machine that makes the crowns. See attached material for content. The flyer should use the practices PMS colors of Green 562 and Blue 3025. The ad should say to the patient - I want to go this office and get my crown done there.
Updates

Project Deadline Extended Reason: The difference in the time zone between USA and Europe has caused issues. Minor changes still need to be worked out. Added Thursday, July 14, 2016

Target Market(s)

Dental Patients

Industry/Entity Type

Dental

Requirements
Must have
• Call to Action
• Business Address and Business Logo
• Classic Design
• images of a Happy 50 year old Couple
• Gives the benefits of the same day crown
Should not have
• No Images of tooth figures
• No before or after pictures

```html
<!DOCTYPE html>
<html lang="en">
<head>
<meta charset="utf-8">
<title>Harbor Dental Care – Same-Day Crowns</title>
<link href="https://fonts.googleapis.com/css2?family=Fira+Sans+Condensed:wght@500;600&family=Fira+Sans:ital,wght@0,500;1,500&family=Open+Sans:wght@300;400;600;700&family=PT+Sans+Narrow&display=swap" rel="stylesheet">
<style>
  :root{
    --page:#f7f7f7;
    --blue-deep:#0a5580;
    --blue-mid:#1b6f9e;
    --blue-text:#1a5c8a;
    --blue-pale:#e6f0f6;
    --green:#148a78;
    --green-dark:#0c6a5c;
    --ink:#1e2a33;
    --white:#ffffff;
  }
  *{margin:0;padding:0;box-sizing:border-box}
  html,body{width:1200px;height:1200px;overflow:hidden;background:var(--page)}
  .stage{position:relative;width:1200px;height:1200px}
  .flyer{position:absolute;left:137px;top:0;width:965px;height:1250px;transform:scale(.96);transform-origin:0 0;background:var(--white);overflow:hidden;font-family:"Open Sans",sans-serif}
  .hero{position:absolute;left:0;top:0;width:965px;height:592px;
    background:linear-gradient(180deg,var(--blue-deep) 0%,#0e5f8d 45%,#5f9cbf 68%,#c6dce9 85%,var(--blue-pale) 100%)}
  .hero-swoosh{position:absolute;left:0;top:0}
  .hero-rule{position:absolute;left:0;top:588px;width:965px;height:5px;background:linear-gradient(90deg,var(--blue-deep),var(--blue-mid))}
  .headline{position:absolute;left:0;top:48px;width:965px;text-align:center;color:var(--white);
    font-family:"Fira Sans Condensed",sans-serif;font-weight:600;font-size:42px;line-height:51px;letter-spacing:.2px;padding-left:20px}
  .hairline{position:absolute;left:180px;top:183px;width:700px;height:1px;background:linear-gradient(90deg,transparent,rgba(255,255,255,.5),transparent)}
  .goodbye{position:absolute;left:0;height:56px;width:470px;display:flex;align-items:center;padding-left:51px;
    color:var(--white);font-family:"Fira Sans Condensed",sans-serif;font-weight:500;font-size:21px;
    background:linear-gradient(90deg,#2aa796 0%,var(--green) 40%,rgba(12,106,92,.7) 80%,rgba(12,106,92,0) 100%);
    border-bottom:3px solid rgba(6,50,60,.55)}
  .intro{position:absolute;left:485px;top:218px;width:450px;color:var(--white);font-size:16px;line-height:22px}
  .intro p{margin-bottom:13px}
  .benefit-lead{position:absolute;left:51px;top:443px;color:var(--blue-text);font-family:"Fira Sans",sans-serif;font-style:italic;font-weight:500;font-size:20px;letter-spacing:.6px}
  .benefit-list{position:absolute;left:51px;top:493px;list-style:none;color:var(--blue-text);font-weight:600;font-size:17px;line-height:23px}
  .result-photos{position:absolute;left:351px;top:492px;width:288px;height:73px;background:var(--white);padding:5px;display:flex;gap:8px}
  .result-photos span{flex:1;background:linear-gradient(180deg,#9a4c3e,#d8b98f 55%,#a3584a)}
  .couple{position:absolute;left:540px;top:595px;width:425px;height:590px;
    background:radial-gradient(ellipse at 62% 35%,#c9b7a4 0%,#d9e4ec 45%,rgba(230,240,246,.6) 70%,rgba(255,255,255,0) 100%),linear-gradient(180deg,#dcecf6 0%,#eef4f7 60%,#ffffff 100%)}
  .couple-curve{position:absolute;left:540px;top:595px}
  .section-title{position:absolute;left:50px;top:652px;color:var(--blue-deep);font-weight:700;font-size:28px;letter-spacing:-.3px}
  .lead{position:absolute;left:50px;top:705px;width:510px;color:var(--blue-text);font-size:16px;line-height:22px}
  .body{position:absolute;left:51px;top:767px;width:494px;color:var(--blue-text);font-size:16px;line-height:22px;text-align:justify}
  .cta{position:absolute;left:50px;top:935px;color:var(--blue-text);font-family:"PT Sans Narrow",sans-serif;font-size:30px}
  .brand{position:absolute;left:48px;top:1128px;color:var(--blue-deep);font-family:"Open Sans",sans-serif;font-weight:300;font-size:40px;letter-spacing:.5px}
  .tagline{position:absolute;left:50px;top:1186px;color:var(--green);font-family:"Open Sans",sans-serif;font-weight:300;font-size:20px}
  .contact{position:absolute;right:48px;top:1163px;text-align:right;color:var(--ink);font-size:17px;line-height:30px}
  .footer-band{position:absolute;left:0;top:1235px;width:965px;height:15px;background:var(--green)}
</style>
</head>
<body>
<main class="stage">
  <article class="flyer">
    <section class="hero">
      <svg class="hero-swoosh" width="965" height="592" viewBox="0 0 965 592" aria-hidden="true">
        <path d="M0 0 H330 C180 60 80 140 0 230 Z" fill="rgba(255,255,255,.18)"/>
        <path d="M0 0 H220 C120 50 40 110 0 160 Z" fill="rgba(255,255,255,.14)"/>
        <path d="M0 300 C150 160 420 80 965 60" stroke="rgba(255,255,255,.12)" stroke-width="2" fill="none"/>
      </svg>
      <h1 class="headline">ARE YOU READY FOR A DRAMATICALLY IMPROVED<br>EXPERIENCE WITH YOUR NEXT CROWN?</h1>
      <div class="hairline"></div>
      <div class="goodbye" style="top:222px">GOOD-BYE TEMPORARY CROWN</div>
      <div class="goodbye" style="top:278px">GOOD-BYE SECOND APPOINTMENT</div>
      <div class="goodbye" style="top:337px">GOOD-BYE GOOEY MESSY IMPRESSIONS</div>
      <div class="intro">
        <p>Harbor Dental Care is pleased to offer you the Comfort and Convenience of One Visit Dental Care.</p>
        <p>We understand how hard it can be to take off work or have someone take care of the kids even once, but twice??</p>
        <p>Now with 3D CADCAM Technology,<br>we can digitally design and mill a Customized,<br>Ceramic Restoration in one appointment.</p>
      </div>
      <p class="benefit-lead">When it comes to your next crown, the benefits of a Digital Restoration add up quickly!</p>
      <ul class="benefit-list">
        <li>A Same-Day Restoration</li>
        <li>A Stronger More Precise Fit</li>
        <li>A Beautiful Natural Appearance</li>
      </ul>
      <div class="result-photos" role="img" aria-label="Two close-up photos of restored teeth"><span></span><span></span></div>
    </section>
    <div class="hero-rule"></div>

    <div class="couple" role="img" aria-label="Photo of a smiling older couple on a sunny beach"></div>
    <svg class="couple-curve" width="425" height="590" viewBox="0 0 425 590" aria-hidden="true">
      <path d="M425 380 C360 500 220 570 60 590 H425 Z" fill="#ffffff"/>
    </svg>

    <h2 class="section-title">SAME-DAY DIGITAL RESTORATIONS.</h2>
    <p class="lead">Crowns, veneers and bridges that happen in hours instead of days.<br>Ask your dentist if digital dentistry is right for you.</p>
    <p class="body">Restorative dentistry has evolved and now, digital technology allows us to take an impression of your teeth with a digital scanner and create your restoration right in our office. We can match your existing teeth and provide you with a filling, veneer, crown or bridge using the most advanced non-metal composite materials giving you a beautiful smile and natural appearance.</p>
    <p class="cta">Find out if digital dentistry is right for you.</p>

    <p class="brand">Harbor Dental Care</p>
    <p class="tagline">It All Begins With a Healthy Smile!</p>
    <address class="contact" style="font-style:normal">Company Address<br>Call to Action | +0123 456789</address>
    <div class="footer-band"></div>
  </article>
</main>
</body>
</html>
```